BRAMLEIGH real estate family office

Hello, Our business is a real estate intermediation activity on high-end goods (amounts exceeding € 10m) for corporate and private clients. You can see our logo on the site www.bramleigh-invented.fr We would like to keep that spirit with the hexagon that represents France (transactions between Monaco and Saint Tropez, Courchevel and Paris). And the "baseline" that is "real estate family office". The corporate logo should be and can be printed by embossing (relief). We must integrate the name, first name, phone, email and website. Finally, to imbibe the spirit of business, here is a detail of the activity. "Genuine consulting firm in real estate investments, BRAMLEIGH works with its customers as a specialized player in the high-end markets, we are recognized for our ultra-confidential approach and tailor-made, as well as the quality of our network. We broadcast any information on the market and we work exclusively through a strong relationship we have developed over the years. BRAMLEIGH is active on the French Riviera (from Monaco to Saint-Tropez), the Alps (Courchevel, Méribel, Megève) and Paris (essentially market premium). Always looking for opportunities for our clients, we work on two investment areas: residential luxury real estate (properties, vineyards, mansions, land, etc.) commercial real estate (empty office buildings or yield, hotel properties, land, etc.) "

Target Market(s)

High foreign end customers. corporate and private.

Industry/Entity Type

Real Estate

Contact Information for Business Card

LOGO
baseline
Laurent Dufossé
+33(0)6.41.57.09.64
ld@bramleigh-invented.fr
www.bramleigh-invented.fr

Font styles to use
Serif

Colors
cedeed
0255a3
3277b5
85abd2
85cae6
34a7d7
0792cd
cfdeed
1b1b1b

Requirements
Must have
• see description

```html
<!DOCTYPE html>
<html lang="fr">
<head>
<meta charset="utf-8">
<title>Bramleigh – business card</title>
<link href="https://fonts.googleapis.com/css2?family=Questrial&display=swap" rel="stylesheet">
<style>
  :root {
    --backdrop: #e9e6e1;
    --card-white: #ffffff;
    --grey-light: #8e8f90;
    --grey-dark: #6b6c6d;
    --brand-blue: #0255a3;
    --band-blue: #1e4aa0;
    --band-blue-dark: #173c86;
    --wordmark-grey: #6f7071;
    --ink-white: #ffffff;
  }
  * { box-sizing: border-box; margin: 0; padding: 0; }
  html, body { width: 1200px; height: 843px; overflow: hidden; }
  body {
    background: var(--backdrop);
    font-family: "Questrial", "Century Gothic", sans-serif;
    display: flex;
    align-items: center;
    justify-content: center;
    gap: 60px;
  }
  .card {
    position: relative;
    width: 520px;
    height: 297px;
    border-radius: 3px;
    overflow: hidden;
    box-shadow: 0 10px 28px rgba(0,0,0,.18);
  }

  /* Back of card */
  .card--back {
    background: linear-gradient(160deg, var(--grey-light), var(--grey-dark));
    color: var(--ink-white);
  }
  .card--back .lockup { position: absolute; left: 0; right: 0; top: 98px; text-align: center; }
  .card--back .wordmark { color: var(--ink-white); }
  .card--back .baseline { color: var(--ink-white); }
  .card--back .website {
    position: absolute; left: 0; right: 0; top: 212px;
    text-align: center; font-size: 12px; letter-spacing: 7px;
  }

  /* Front of card */
  .card--front { background: var(--card-white); }
  .card--front .lockup { position: absolute; left: 0; right: 0; top: 54px; text-align: center; }
  .card--front .wordmark { color: var(--wordmark-grey); }
  .card--front .baseline { color: var(--brand-blue); }
  .band { position: absolute; left: 0; top: 0; width: 520px; height: 297px; }
  .contact {
    position: absolute; left: 0; right: 0; top: 178px;
    text-align: center; color: var(--ink-white);
  }
  .contact__name { font-size: 17px; font-weight: 400; letter-spacing: .5px; margin-bottom: 10px; }
  .contact__line { font-size: 12.5px; line-height: 19px; }
  .contact__role { font-size: 13px; line-height: 20px; }

  /* Shared lockup */
  .wordmark {
    font-size: 40px; letter-spacing: 5px; line-height: 1;
    display: inline-flex; align-items: center; gap: 14px;
  }
  .wordmark__mark { width: 12px; height: 12px; background: currentColor; display: inline-block; }
  .baseline { display: block; font-size: 14px; letter-spacing: 1px; margin-top: 6px; padding-left: 120px; }
</style>
</head>
<body>
  <section class="card card--back" aria-label="Card back">
    <div class="lockup">
      <span class="wordmark"><span class="wordmark__mark"></span>BRAMLEIGH</span>
      <span class="baseline">real estate family office</span>
    </div>
    <p class="website">www.bramleigh-invented.fr</p>
  </section>

  <section class="card card--front" aria-label="Card front">
    <svg class="band" viewBox="0 0 520 297" aria-hidden="true">
      <defs>
        <linearGradient id="bandFill" x1="0" y1="0" x2="1" y2="1">
          <stop offset="0" stop-color="var(--band-blue)"/>
          <stop offset="1" stop-color="var(--band-blue-dark)"/>
        </linearGradient>
      </defs>
      <polygon points="0,165 455,165 520,297 68,297" fill="url(#bandFill)"/>
    </svg>
    <div class="lockup">
      <span class="wordmark"><span class="wordmark__mark"></span>BRAMLEIGH</span>
      <span class="baseline">real estate family office</span>
    </div>
    <div class="contact">
      <p class="contact__name">Laurent Dufossé</p>
      <p class="contact__line">P : +33(0)6.41.57.09.64</p>
      <p class="contact__line">E : ld@bramleigh-invented.fr &nbsp; W : www.bramleigh-invented.fr</p>
      <p class="contact__role">Real estate family office</p>
    </div>
  </section>
</body>
</html>
```